Melbourne Locksmith Needs a Web Site

We need a web site for our new Locksmith business in Melbourne Australia. Our business is called " Calloway Lane Locksmiths" . (Calloway lane is a well known in the city and has the famous railway station , it is a main icon of melbourne . Maybe we could incorperate the station maybe in the front page or heading background. our services include Automotive Locksmithing ( Cuting keys to cars, opening cars etc / Master Keys Systems/ Commercial work / Domestic . Also we have no logo yet. but we can get that in the future if needed.

Target Market(s)

(Automotive ) Lost keys to cars, Trucks, Jammed Ignitions, Opening Vehicles. mobile locksmith in a van, Locked out of your house ?

Industry/Entity Type

Business

Number of Pages Required

4 page

Font styles to use
Sans Serif

Colors

Designer to choose colors to be used in the design.

Requirements
Must have
• Phone number easy to read on web site.
Nice to have
• map of where we are, show case pictures of common lock problems for automotive eg ( damaged keys/ Broken).

```html
<!DOCTYPE html>
<html lang="en">
<head>
<meta charset="utf-8">
<title>Calloway Lane Locksmiths</title>
<link href="https://fonts.googleapis.com/css2?family=Oswald:wght@400;500&family=Open+Sans:wght@400;600&display=swap" rel="stylesheet">
<style>
:root{
  --green:#1db386;
  --green-dark:#169a73;
  --ink:#222;
  --text:#555;
  --muted:#999;
  --line:#ddd;
  --white:#fff;
  --night:#12151a;
  --night-deep:#0b0d10;
}
*{box-sizing:border-box;margin:0;padding:0}
html,body{width:1200px;height:2795px;overflow:hidden}
body{position:relative;background:var(--white);font-family:"Open Sans",Arial,sans-serif;color:var(--text)}

/* header */
.site-header{position:absolute;left:0;top:0;width:1200px;height:130px;background:var(--white);border-top:5px solid var(--green)}
.brand{position:absolute;left:93px;top:24px;font-family:"Oswald",sans-serif;font-weight:500;color:var(--green);font-size:31px;line-height:34px;letter-spacing:1px;text-transform:uppercase}
.brand span{display:block}
.brand .wide{letter-spacing:4.2px}
.phone{position:absolute;left:808px;top:25px;font-size:21px;color:var(--ink);display:flex;align-items:center;gap:10px}
.social-top{position:absolute;left:987px;top:28px;display:flex;gap:10px}
.social-top i{display:block;width:21px;height:21px;background:var(--green);border-radius:3px}
.main-nav{position:absolute;left:460px;top:66px;display:flex;align-items:center;font-size:15px;color:var(--ink)}
.main-nav a{text-decoration:none;color:inherit;text-transform:uppercase}
.main-nav .active{background:var(--green);color:var(--white);border-radius:20px;padding:7px 28px}
.main-nav .n-about{margin-left:18px}
.main-nav .n-services{margin-left:38px}
.main-nav .n-products{margin-left:37px}
.main-nav .n-blog{margin-left:37px}
.main-nav .n-contact{margin-left:37px}

/* hero */
.hero{position:absolute;left:0;top:130px;width:1200px;height:509px;background:linear-gradient(180deg,#8ea2b4 0%,#b9a996 45%,#6d6a55 75%,#3d4330 100%)}
.hero h1{position:absolute;left:0;width:1200px;top:228px;text-align:center;font-family:"Oswald",sans-serif;font-weight:400;font-size:56px;line-height:66px;color:var(--white);text-transform:uppercase}
.hero p{position:absolute;left:0;width:1200px;top:294px;text-align:center;font-size:36px;color:var(--white)}
.hero-arrows{position:absolute;left:1050px;top:450px}

/* welcome */
.welcome h2{position:absolute;left:0;width:1200px;top:722px;text-align:center;font-weight:400;font-size:27px;color:var(--ink);text-transform:uppercase}
.welcome .lead{position:absolute;left:112px;width:976px;top:768px;text-align:center;font-size:15px;line-height:22px;color:var(--muted)}
.service-card{position:absolute;top:862px;width:293px;height:218px;border:1px solid var(--line);box-shadow:0 2px 4px rgba(0,0,0,.12);background:var(--white);text-align:center}
.service-card.featured{background:var(--green);border-color:var(--green);color:var(--white)}
.service-card svg{position:absolute;left:121px;top:32px}
.service-card h3{position:absolute;left:0;width:100%;top:102px;font-weight:400;font-size:15px;color:var(--ink);text-transform:uppercase}
.service-card.featured h3,.service-card.featured p{color:var(--white)}
.service-card p{position:absolute;left:20px;right:20px;top:127px;font-size:12px;line-height:18px;color:var(--muted)}
.btn-small{position:absolute;left:100px;top:173px;width:93px;height:21px;border:1px solid #aaa;border-radius:11px;font-size:11px;line-height:19px;color:var(--text);background:var(--white)}

/* what we do */
.what-we-do{position:absolute;left:0;top:1170px;width:1200px;height:458px;background:linear-gradient(180deg,#161b22,#0f1216)}
.wwd-box{position:absolute;left:147px;top:74px;width:488px;height:326px;background:var(--white)}
.wwd-box h2{position:absolute;left:37px;top:50px;font-weight:400;font-size:30px;color:var(--ink);text-transform:uppercase}
.wwd-box .sub{position:absolute;left:37px;top:92px;font-size:16px;color:var(--text)}
.wwd-box .body{position:absolute;left:37px;width:420px;top:130px;font-size:13px;line-height:25px;text-align:justify;color:var(--text)}
.btn-green{position:absolute;left:39px;top:266px;width:110px;height:34px;border-radius:17px;background:var(--green);color:var(--white);font-size:13px;line-height:34px;text-align:center;text-transform:uppercase}
.wwd-media{position:absolute;left:635px;top:74px;width:408px;height:326px;background:linear-gradient(135deg,#6d7d6a,#3a3d3c 55%,#c9c9c9)}
.wwd-media svg{position:absolute;left:180px;top:134px}

/* works */
.works h2{position:absolute;left:0;width:1200px;top:1694px;text-align:center;font-weight:400;font-size:31px;color:var(--ink);text-transform:uppercase}
.work-card{position:absolute;top:1777px;height:274px;box-shadow:0 2px 4px rgba(0,0,0,.15);background:var(--white)}
.work-card .photo{height:222px}
.work-card .label{height:52px;border:1px solid var(--line);border-top:none;text-align:center;font-size:16px;line-height:52px;color:var(--ink);text-transform:uppercase}
.works .arrow{position:absolute;top:1897px}

/* location */
.location-band{position:absolute;left:0;top:2133px;width:1200px;height:56px;background:var(--green);color:var(--white);text-align:center;font-size:27px;line-height:56px;text-transform:uppercase}
.map{position:absolute;left:0;top:2189px;width:1200px;height:293px;background:linear-gradient(160deg,#e6e6e6,#d9d9d9 60%,#e3e3e3)}

/* footer */
.site-footer{position:absolute;left:0;top:2482px;width:1200px;height:249px;background:var(--night)}
.footer-brand{position:absolute;left:93px;top:96px;font-family:"Oswald",sans-serif;font-weight:500;color:var(--white);font-size:29px;line-height:31px;letter-spacing:1px;text-transform:uppercase}
.footer-brand span{display:block}
.footer-brand .wide{letter-spacing:3.8px}
.site-footer h4{position:absolute;font-weight:400;font-size:17px;color:var(--white);text-transform:uppercase}
.site-footer .small{position:absolute;font-size:13px;line-height:24px;color:var(--white)}
.email-input{position:absolute;left:384px;top:143px;width:214px;height:30px;background:#eee;font-size:12px;line-height:30px;padding-left:9px;color:#888}
.btn-subscribe{position:absolute;left:384px;top:188px;width:95px;height:30px;background:var(--green);color:var(--white);font-size:12px;line-height:30px;text-align:center;text-transform:uppercase}
.follow-item{position:absolute;left:963px;display:flex;align-items:center;gap:17px;font-size:13px;color:var(--white)}
.follow-item i{display:block;width:34px;height:34px;border:1.5px solid var(--white);border-radius:50%}
.footer-bottom{position:absolute;left:0;top:2731px;width:1200px;height:64px;background:var(--night-deep);text-align:center;font-size:12px;line-height:64px;color:var(--white)}
</style>
</head>
<body>

<header class="site-header">
  <div class="brand"><span>Calloway Lane</span><span class="wide">Locksmiths</span></div>
  <div class="phone">
    <svg width="18" height="18" viewBox="0 0 24 24"><path fill="#1db386" d="M6.6 10.8a15 15 0 0 0 6.6 6.6l2.2-2.2c.3-.3.7-.4 1-.2 1.1.4 2.3.6 3.6.6.6 0 1 .4 1 1V20c0 .6-.4 1-1 1A17 17 0 0 1 3 4c0-.6.4-1 1-1h3.5c.6 0 1 .4 1 1 0 1.3.2 2.5.6 3.6.1.3 0 .7-.2 1z"/></svg>
    555 014 2290
  </div>
  <div class="social-top"><i></i><i></i><i></i><i></i></div>
  <nav class="main-nav">
    <a class="active">Home</a>
    <a class="n-about">About</a>
    <a class="n-services">Services</a>
    <a class="n-products">Products</a>
    <a class="n-blog">Blog</a>
    <a class="n-contact">Contact Us</a>
  </nav>
</header>

<section class="hero" role="img" aria-label="City skyline at dusk with the historic railway station and river bridge">
  <h1>Jammed Ignitions</h1>
  <p>Locked out of your house ?</p>
  <svg class="hero-arrows" width="40" height="24" viewBox="0 0 40 24"><path d="M10 6l-6 6 6 6M30 6l6 6-6 6" stroke="#fff" stroke-width="2" fill="none"/></svg>
</section>

<section class="welcome">
  <h2>Welcome to Calloway Lane Locksmiths</h2>
  <p class="lead">It is a long established fact that a reader will be distracted by the readable content of a page when looking at its layout. The point of using Lorem Ipsum is that it has a more-or-less normal distribution of letters, as opposed to using 'Content here, content here</p>

  <div class="service-card" style="left:127px">
    <svg width="50" height="56" viewBox="0 0 50 56"><circle cx="18" cy="9" r="7" fill="none" stroke="#1db386" stroke-width="4"/><path d="M25 9h16v6M35 9v5" stroke="#1db386" stroke-width="4" fill="none"/><path d="M6 36l5-11h28l5 11v14h-7v-5H13v5H6z" fill="#1db386"/><circle cx="14" cy="39" r="3" fill="#fff"/><circle cx="36" cy="39" r="3" fill="#fff"/></svg>
    <h3>Cuting keys to cars</h3>
    <p>It has survived not only five centuries, but also the leap into electronic</p>
    <div class="btn-small">View More</div>
  </div>
  <div class="service-card featured" style="left:456px">
    <svg width="50" height="56" viewBox="0 0 50 56"><circle cx="16" cy="14" r="10" fill="none" stroke="#fff" stroke-width="4"/><rect x="20" y="22" width="14" height="18" rx="3" transform="rotate(-30 27 31)" fill="#fff"/><path d="M33 36l10 14M38 44l4-3" stroke="#fff" stroke-width="4"/></svg>
    <h3>Master Keys Systems</h3>
    <p>It has survived not only five centuries, but also the leap into electronic</p>
    <div class="btn-small">View More</div>
  </div>
  <div class="service-card" style="left:784px">
    <svg width="50" height="56" viewBox="0 0 50 56"><circle cx="34" cy="12" r="7" fill="none" stroke="#1db386" stroke-width="4"/><path d="M29 17L19 31M22 27l4 3" stroke="#1db386" stroke-width="4"/><path d="M4 36h10l12 6h14c2 0 2 4 0 4H24v3h18l6-6v8L40 56H4z" fill="#1db386"/></svg>
    <h3>Commercial Work</h3>
    <p>It has survived not only five centuries, but also the leap into electronic</p>
    <div class="btn-small">View More</div>
  </div>
</section>

<section class="what-we-do" role="img" aria-label="Dark city skyline background">
  <div class="wwd-box">
    <h2>What We Do</h2>
    <p class="sub">Neque porro quisquam dolorem ipsum</p>
    <p class="body">It is a long established fact that a reader will be distracted by the readable content of a page when looking at its layout. The point of using Lorem Ipsum is that it has a more-or-less normal distribution of letters, as opposed to using 'Content here, content here'.</p>
    <div class="btn-green">Read More</div>
  </div>
  <div class="wwd-media" role="img" aria-label="Video still of a locksmith working on a car door lock">
    <svg width="54" height="54" viewBox="0 0 54 54"><circle cx="27" cy="27" r="26" fill="rgba(40,40,40,.75)"/><path d="M21 16l17 11-17 11z" fill="#fff"/></svg>
  </div>
</section>

<section class="works">
  <h2>Our Works</h2>
  <svg class="arrow" style="left:44px" width="20" height="36" viewBox="0 0 20 36"><path d="M17 2L3 18l14 16" stroke="#999" stroke-width="1.5" fill="none"/></svg>
  <div class="work-card" style="left:89px;width:336px">
    <div class="photo" role="img" aria-label="Car key fob inserted in an ignition, black and white" style="background:linear-gradient(135deg,#2a2a2a,#8a8a8a 60%,#dcdcdc)"></div>
    <div class="label">Master Keys</div>
  </div>
  <div class="work-card" style="left:436px;width:333px">
    <div class="photo" role="img" aria-label="Flip car key on a white surface" style="background:linear-gradient(135deg,#ffffff,#d9d9d9 55%,#9a9a9a)"></div>
    <div class="label">Car Key</div>
  </div>
  <div class="work-card" style="left:779px;width:335px">
    <div class="photo" role="img" aria-label="Freshly cut house keys on a wooden table" style="background:linear-gradient(135deg,#8a6a4e,#b9a38c 50%,#6e5440)"></div>
    <div class="label">Cuting Keys</div>
  </div>
  <svg class="arrow" style="left:1128px" width="20" height="36" viewBox="0 0 20 36"><path d="M3 2l14 16L3 34" stroke="#999" stroke-width="1.5" fill="none"/></svg>
</section>

<div class="location-band">Location</div>
<div class="map" role="img" aria-label="Street map showing the shop locations"></div>

<footer class="site-footer">
  <div class="footer-brand"><span>Calloway Lane</span><span class="wide">Locksmiths</span></div>

  <h4 style="left:382px;top:63px">Newsletters Sign Up</h4>
  <p class="small" style="left:382px;top:96px;width:240px;line-height:17px">Sign up for our daily email by entering your information below</p>
  <div class="email-input">Email address</div>
  <div class="btn-subscribe">Subscribe</div>

  <h4 style="left:723px;top:61px">Get in Touch</h4>
  <p class="small" style="left:723px;top:99px;line-height:26px">Address : 88 Harrow St<br>Brookvale, VIC 3999<br>Phone : 555-019-4471<br>Email : info@callowaylane.example</p>

  <h4 style="left:963px;top:52px">Follow Us On</h4>
  <div class="follow-item" style="top:97px"><i></i>Circlebook</div>
  <div class="follow-item" style="top:141px"><i></i>Chirper</div>
  <div class="follow-item" style="top:184px"><i></i>Snapgram</div>
</footer>
<div class="footer-bottom">Copyright © 2017. All Rights Reserved</div>

</body>
</html>
```